Chimney Service company needs new business card design

We need a updated business card with our new logo added. We provide a full range of chimney services throughout Vermont and New Hampshire. The business card will be one sided and color. Attached is our current business card another document showing all the information we would like on the card.
We dont like a lot of flashy colors.... here is a link to our website to get an idea of our branding www.flueguardianvt.example

Target Market(s)

homeowners

Industry/Entity Type

Business

Contact Information for Business Card

See attached sheet for content.

Font styles to use
Serif
Sans Serif

Requirements
Must have
• all information provided on separate sheet
Should not have
• Additional information that may clogg up design

```html
<!DOCTYPE html>
<html lang="en">
<head>
<meta charset="utf-8">
<title>Flue Guardian – Business Card</title>
<link rel="stylesheet" href="https://fonts.googleapis.com/css2?family=Sorts+Mill+Goudy&display=swap">
<style>
  :root {
    --paper: #ffffff;
    --charcoal: #222627;
    --ink: #2b2b2b;
    --light: #f4f4f2;
  }
  * { margin: 0; padding: 0; box-sizing: border-box; }
  html, body { width: 687px; height: 1200px; overflow: hidden; background: var(--paper); }
  .card {
    position: relative;
    width: 687px;
    height: 1200px;
    font-family: "Sorts Mill Goudy", Georgia, serif;
    background: var(--paper);
    border: 1px solid #d8d8d8;
  }
  .brand {
    position: absolute;
    inset: 0 0 auto 0;
    height: 479px;
    text-align: center;
  }
  .brand-mark {
    position: absolute;
    left: 228px;
    top: 88px;
    width: 234px;
    height: 236px;
  }
  .brand-name {
    position: absolute;
    left: 0;
    right: 0;
    top: 364px;
    font-size: 62px;
    font-weight: 400;
    letter-spacing: 3px;
    color: var(--ink);
    text-transform: uppercase;
    line-height: 1;
    white-space: nowrap;
  }
  .details {
    position: absolute;
    inset: 479px 0 0 0;
    background: var(--charcoal);
    color: var(--light);
    text-align: center;
  }
  .services { list-style: none; }
  .line { position: absolute; left: 0; right: 0; line-height: 1; white-space: nowrap; }
  .intro { font-size: 27px; }
  .service { font-size: 31px; text-transform: uppercase; letter-spacing: 0.3px; }
  .contact { font-size: 30px; }
  .rule {
    position: absolute;
    left: 312px;
    width: 63px;
    background: var(--light);
  }
  .rule-thin { height: 1px; }
  .rule-bold { height: 4px; }
</style>
</head>
<body>
<div class="card">
  <header class="brand">
    <svg class="brand-mark" viewBox="0 0 234 236" aria-hidden="true">
      <rect x="9" y="9" width="216" height="218" fill="none" stroke="#2b2b2b" stroke-width="18"/>
    </svg>
    <h1 class="brand-name">Flue Guardian</h1>
  </header>

  <section class="details">
    <p class="line intro" style="top:44px">Serving VT &amp; New Hampshire since 1989</p>
    <p class="line intro" style="top:84px">Fully Insured – Free Estimates</p>
    <p class="line intro" style="top:123px">Family Owned &amp; Operated</p>

    <div class="rule rule-thin" style="top:191px"></div>

    <ul class="services">
      <li class="line service" style="top:240px">Full Masonry Services</li>
      <li class="line service" style="top:286px">Historic Chimney Restoration</li>
      <li class="line service" style="top:332px">Stainless Steel Liners</li>
      <li class="line service" style="top:377px">New Chimney Installations</li>
      <li class="line service" style="top:423px">VFSB Certified Chimney Sweeps</li>
    </ul>

    <div class="rule rule-bold" style="top:497px"></div>

    <address class="contact-block" style="font-style:normal">
      <p class="line contact" style="top:543px">802-555-0147</p>
      <p class="line contact" style="top:589px">info@flueguardianvt.example</p>
      <p class="line contact" style="top:634px">www.flueguardianvt.example</p>
    </address>
  </section>
</div>
</body>
</html>
```